Retail Sign for Houseplant Campaign

Sign will measure 3 to 4 foot tall by 22.2inches and place on rolling racks of houseplants for a retail promotion in The Brickfield Yard. The theme of the promotion will be "New Year, New You!" Selling points which should be on the sign are Houseplants give you a taste of nature, Houseplants boost air quality inside your home, Indoor plants reduce anxiety, Indoor plants make you more productive, Houseplants improve your concentration and memory.
Updates

Target Market(s)

People who love plants

Industry/Entity Type

Horticulture/ retail

Colors
00AB8E
00BBA5
67D7C9
C6EFE9
E9F9F6
59FF00
82FF00
B8FF75
E3FFCB
F4FFEA
FFF300
FFF600
FEFA6F
FFFEC7
FFFEE8

Requirements
Must have
• Must feel energetic and encourage people to buy plants. Should include 1-2 photos and the selling points listed

```html
<!DOCTYPE html>
<html lang="en">
<head>
<meta charset="utf-8">
<title>New Year New You – Houseplant Sign</title>
<link rel="stylesheet" href="https://fonts.googleapis.com/css2?family=Great+Vibes&family=Roboto+Condensed:wght@400&display=swap">
<style>
  :root {
    --page-bg: #eef0ef;
    --green-light: #2f7d58;
    --green-mid: #225f45;
    --green-dark: #17483a;
    --pine: #1e5a3c;
    --gold: #d9a545;
    --white: #ffffff;
    --rule: rgba(255,255,255,0.35);
    --photo-skin: #c9a58a;
    --photo-wood: #b88e62;
  }
  * { margin: 0; padding: 0; box-sizing: border-box; }
  html, body { width: 1200px; height: 868px; overflow: hidden; background: var(--page-bg); }
  .sign {
    position: absolute; left: 395px; top: 24px; width: 410px; height: 820px;
    overflow: hidden;
    background: linear-gradient(135deg, var(--green-light) 0%, var(--green-mid) 50%, var(--green-dark) 100%);
    font-family: "Roboto Condensed", sans-serif; color: var(--white);
  }
  .pine-top {
    position: absolute; right: 0; top: 0; width: 200px; height: 120px;
    background: radial-gradient(ellipse at 90% 10%, var(--pine) 0%, rgba(30,90,60,0.4) 60%, transparent 75%);
  }
  .pine-bottom {
    position: absolute; left: 0; bottom: 0; width: 130px; height: 130px;
    background: radial-gradient(ellipse at 10% 90%, var(--pine) 0%, rgba(30,90,60,0.4) 55%, transparent 75%);
  }
  .stars { position: absolute; inset: 0; pointer-events: none; }
  .headline {
    position: absolute; left: 40px; top: 80px; width: 340px;
    font-family: "Great Vibes", cursive; font-weight: 400; line-height: 1;
  }
  .headline .line-one { display: block; font-size: 78px; padding-left: 12px; }
  .headline .line-two { display: block; font-size: 54px; padding-left: 90px; margin-top: 4px; }
  .benefits { position: absolute; left: 36px; top: 298px; width: 280px; list-style: none; }
  .benefits li {
    display: flex; align-items: center; gap: 6px;
    font-size: 12.5px; height: 27px;
    border-bottom: 1px solid var(--rule);
  }
  .benefits li:last-child { border-bottom: none; }
  .benefits svg { flex: none; }
  .photo-person {
    position: absolute; right: 0; top: 318px; width: 122px; height: 502px;
    background: linear-gradient(180deg, #5a3a2a 0%, var(--photo-skin) 30%, #c9a58a 60%, #2b2b2b 100%);
    border-radius: 50px 0 0 0;
  }
  .photo-plant {
    position: absolute; left: 44px; top: 430px; width: 246px; height: 390px;
    background: linear-gradient(180deg, #c2553f 0%, #d9b27a 30%, #f2f2f0 50%, var(--photo-wood) 75%, #7e8b8a 100%);
  }
</style>
</head>
<body>
  <main class="sign">
    <div class="pine-top" role="img" aria-label="Pine branch decoration"></div>
    <div class="pine-bottom" role="img" aria-label="Pine branch decoration"></div>

    <svg class="stars" width="410" height="820" viewBox="0 0 410 820" aria-hidden="true">
      <g fill="var(--gold)">
        <polygon points="190,20 197,38 216,38 201,49 207,67 190,56 173,67 179,49 164,38 183,38"/>
        <polygon points="370,122 378,145 402,145 383,159 390,182 370,168 350,182 357,159 338,145 362,145"/>
        <polygon points="310,190 313,198 321,198 315,203 317,211 310,206 303,211 305,203 299,198 307,198"/>
        <polygon points="338,212 342,222 352,222 344,228 347,238 338,232 329,238 332,228 324,222 334,222"/>
        <polygon points="10,660 13,668 21,668 15,673 17,681 10,676 3,681 5,673 -1,668 7,668"/>
      </g>
    </svg>

    <h1 class="headline">
      <span class="line-one">New Year</span>
      <span class="line-two">new you!</span>
    </h1>

    <ul class="benefits">
      <li><svg width="12" height="12" viewBox="0 0 12 12"><circle cx="6" cy="6" r="5.2" fill="none" stroke="#fff" stroke-width="1.2"/><path d="M3.5 6.2l1.8 1.8 3.3-3.6" fill="none" stroke="#fff" stroke-width="1.2"/></svg>Houseplants boost air quality inside your home</li>
      <li><svg width="12" height="12" viewBox="0 0 12 12"><circle cx="6" cy="6" r="5.2" fill="none" stroke="#fff" stroke-width="1.2"/><path d="M3.5 6.2l1.8 1.8 3.3-3.6" fill="none" stroke="#fff" stroke-width="1.2"/></svg>Indoor plants reduce anxiety</li>
      <li><svg width="12" height="12" viewBox="0 0 12 12"><circle cx="6" cy="6" r="5.2" fill="none" stroke="#fff" stroke-width="1.2"/><path d="M3.5 6.2l1.8 1.8 3.3-3.6" fill="none" stroke="#fff" stroke-width="1.2"/></svg>Indoor plants make you more productive</li>
      <li><svg width="12" height="12" viewBox="0 0 12 12"><circle cx="6" cy="6" r="5.2" fill="none" stroke="#fff" stroke-width="1.2"/><path d="M3.5 6.2l1.8 1.8 3.3-3.6" fill="none" stroke="#fff" stroke-width="1.2"/></svg>Houseplants improve your concentration and memory</li>
    </ul>

    <div class="photo-plant" role="img" aria-label="Photo of a potted croton plant in a woven basket on a white side table with a lantern"></div>
    <div class="photo-person" role="img" aria-label="Photo of a smiling woman placing a houseplant on a table"></div>
  </main>
</body>
</html>
```